First Website for Lanternfield Advisory Group

We need a great new website design to flow with our brand identity (attached; developed here on PixelHarbor just recently). It needs to be professional, but with just a little bit of fun thrown in, to reflect the caribbean location of our business. The logo already achieves this and thus it should flow from there.

The site will have a few primary sections:

Home - self explanatory, and overview of our business and some of the most recent posts from the next section
Notes - Really just a fancy word for a blog, it will be an ordered set of posts on various regulatory and business news items relevant to Caribbean businesses
"Start/Relocate a Consulting Practice?" or "Become a Partner" - A section on how to bring a consulting practice, new or old, into the partnership and the tax and regulatory advantages of doing so
Contact - Self explanatory

So, it needs a navigation that supports that sparse set of top level links, and a basic design for home, one interior page like "Become a Partner", and the blog/Notes section, that my developer can work from.

UPDATE: I like the designs that have brought in the logo colors to make each sub-page uniquely colored. But, all so far rely too heavily on smiling photos of people. 1) Notes will not have photos to go with them (this is going to be mostly legal updates, tax info, etc.) 2) For the hero photon on the home page, it shouldn't be too high, and should probably be a photo of a beach, preferably one from Puerto Rico where we are located. 3) There should be no search and no social media buttons - the design is meant to be sparse on purpose and we have no need for those items.

Other than the logo, please stick to web safe or google web fonts for text, and have them specified in the source format during delivery. Thanks.

Target Market(s)

Business owners. Often in high tech fields. As well as high net worth family offices.

Industry/Entity Type

Legal

Requirements
Must have
• Must pull in colors from the logo effectively, without looking garish or overly bright.

```html
<!DOCTYPE html>
<html lang="en">
<head>
<meta charset="utf-8">
<title>Lanternfield Advisory Group</title>
<link href="https://fonts.googleapis.com/css2?family=Open+Sans:wght@400;600;700&family=Oswald:wght@400;500&family=PT+Sans+Narrow:wght@400;700&display=swap" rel="stylesheet">
<style>
:root{
  --red:#c8102e;
  --green:#3ec43a;
  --lime:#9ccc12;
  --blue:#1fa7d6;
  --sky:#29b2dd;
  --ink:#333;
  --grey:#555;
  --panel:#ececec;
  --field:#f7f7f7;
  --line:#cfcfcf;
}
*{margin:0;padding:0;box-sizing:border-box}
html,body{width:1200px;height:2362px;overflow:hidden}
body{position:relative;background:#fff;font-family:"Open Sans",Arial,sans-serif;color:var(--ink)}
.abs{position:absolute}

/* header */
.nav-bar{left:0;top:96px;width:1200px;height:32px;background:var(--red)}
.brand{left:123px;top:0;width:357px;height:128px;background:#fff;box-shadow:0 0 12px rgba(0,0,0,.25);display:flex;align-items:center;justify-content:center;gap:10px}
.brand-dot{width:14px;height:14px;border-radius:50%;background:var(--blue)}
.brand-name{font-weight:700;font-size:21px;color:var(--red);white-space:nowrap}
.nav{left:480px;top:96px;height:32px;display:flex;align-items:center}
.nav a{position:absolute;color:#fff;text-decoration:none;font-size:14px;white-space:nowrap;transform:translateX(-50%)}
.contact-top{right:128px;top:12px;text-align:right}
.contact-top .lead{font-family:Arial,sans-serif;font-size:12px;color:#222}
.contact-top .phone{font-family:"Oswald",sans-serif;font-weight:500;font-size:33px;color:var(--green);line-height:40px;display:flex;align-items:center;justify-content:flex-end;gap:6px}
.contact-top .mail{font-family:Arial,sans-serif;font-size:12px;color:var(--blue)}

/* hero */
.hero{left:0;top:128px;width:1200px;height:497px;background:linear-gradient(180deg,#8fc3e6 0%,#cfe4f2 30%,#2b8fb0 48%,#1d7b98 70%,#e2c08c 86%,#d7ad74 100%)}
.hero-title{left:444px;top:256px;width:368px;text-align:center;font-family:"Oswald",sans-serif;font-weight:500;font-size:50px;letter-spacing:-1.5px;color:#fff;line-height:60px;white-space:nowrap}
.hero-text{left:448px;top:320px;width:500px;text-align:center;color:#fff;font-size:14px;line-height:17px}
.hero-more{left:496px;top:378px;font-family:"Oswald",sans-serif;font-weight:500;font-size:25px;letter-spacing:-.5px;color:var(--sky);display:flex;align-items:center;gap:6px}

/* welcome */
.welcome{left:140px;top:562px;width:920px;height:257px;background:var(--panel);box-shadow:0 6px 14px rgba(0,0,0,.15)}
.welcome-photo{left:27px;top:22px;width:265px;height:214px;background:linear-gradient(135deg,#dfe3e6,#8f969c 60%,#5b6066)}
.welcome-title{left:320px;top:36px;font-size:23px;font-weight:600;color:var(--ink);white-space:nowrap}
.welcome-title span{color:var(--blue)}
.welcome-text{left:320px;width:550px;font-size:14px;line-height:17px;color:var(--ink)}
.read-more{left:320px;top:195px;font-size:12.5px;font-weight:700;color:var(--green);display:flex;align-items:center;gap:10px}

/* news */
.post{width:400px;height:100px}
.post-date{left:0;top:0;width:44px;height:66px}
.post-month{left:0;top:46px;width:44px;text-align:center;font-family:"Oswald",sans-serif;font-size:17px;color:var(--blue);line-height:20px}
.post-title{left:60px;top:-2px;font-family:"PT Sans Narrow",sans-serif;font-weight:700;font-size:17px;color:var(--red);white-space:nowrap}
.post-body{left:60px;top:22px;width:340px;font-family:"PT Sans Narrow",sans-serif;font-size:13.5px;line-height:15.5px;color:#333}

/* testimonials */
.testimonials{left:0;top:1252px;width:1200px;height:430px;background:radial-gradient(ellipse at 40% 40%,#b9dc3a 0%,#9fcc14 55%,#8dbd0b 100%)}
.section-title-light{left:0;top:40px;width:1200px;text-align:center;color:#fff;font-size:35px;font-weight:400}
.avatar{width:100px;height:100px;border-radius:50%;background:#d8c2ac;border:3px solid #fff}
.quote{width:275px;color:#fff}
.quote-mark{font-family:Georgia,serif;font-size:30px;font-weight:700;line-height:20px}
.quote-text{font-size:14px;line-height:16.5px}
.quote-name{margin-top:12px;font-family:Arial,sans-serif;font-weight:700;font-size:15px;color:#4b6a05}
.quote-role{font-family:Arial,sans-serif;font-size:11.5px}

/* contact */
.contact-title{left:0;top:1735px;width:1200px;text-align:center;font-size:50px;font-weight:400;color:var(--grey);line-height:64px}
.contact-sub{left:0;top:1800px;width:1200px;text-align:center;font-size:16px;color:#888}
.field{border:1px solid var(--line);background:var(--field);font-family:Arial,sans-serif;font-size:13px;color:#444;padding:20px 12px}
.send{background:#8e8e8e;display:flex;align-items:center;justify-content:center}

/* footer */
.footer{left:0;top:2134px;width:1200px;height:228px;background:var(--sky);color:#fff;font-family:Arial,sans-serif}
.foot-h{font-size:16px}
.foot-h b{font-weight:700}
.foot-text{font-size:12px;line-height:14px;color:#eaf7fc}
.sub-input{background:#b9ecf8;border:1px solid #8fdbf0}
.sub-btn{background:var(--green);color:#fff;font-size:14px;display:flex;align-items:center;justify-content:center}
.foot-links{font-size:12px;display:flex;gap:14px}
</style>
</head>
<body>

<header>
  <div class="abs nav-bar"></div>
  <div class="abs brand"><span class="brand-dot"></span><span class="brand-name">Lanternfield Advisory Group</span></div>
  <nav class="abs nav">
    <a style="left:70px">HOME</a>
    <a style="left:213px">BECOME A PARTNER</a>
    <a style="left:378px">NEWS / BLOG</a>
    <a style="left:520px">CONTACT US</a>
  </nav>
  <div class="abs contact-top">
    <div class="lead">For questions and inquries contact us</div>
    <div class="phone">
      <svg width="28" height="28" viewBox="0 0 28 28"><circle cx="14" cy="14" r="12" fill="none" stroke="var(--green)" stroke-width="2.5"/><path d="M9 8l3 0 1 4-2 1.5c1 2 2.5 3.5 4.5 4.5L17 16l4 1 0 3c-6 1-13-6-12-12z" fill="var(--green)"/></svg>
      0.555.010.246
    </div>
    <div class="mail">&#9993; info@lanternfieldadvisory.com</div>
  </div>
</header>

<section>
  <div class="abs hero" role="img" aria-label="Tropical beach with turquoise sea, white clouds and palm fronds"></div>
  <h1 class="abs hero-title">BECOME A PARTNER</h1>
  <p class="abs hero-text">Lorem ipsum dolor sit amet, consectetur adipisicing elit, sed do eiusmod tempor incididunt ut labore et dolore magna aliqua incididunt ut labore et dolore magna aliqua. Ut enim ad minimveniam, quis nostrud laboris.</p>
  <div class="abs hero-more">
    <svg width="24" height="18" viewBox="0 0 24 18"><path d="M1 9h19M13 2l8 7-8 7" fill="none" stroke="var(--sky)" stroke-width="3"/></svg>
    MORE INFO
  </div>
</section>

<section class="abs welcome">
  <div class="abs welcome-photo" role="img" aria-label="Business people shaking hands at a meeting table"></div>
  <h2 class="abs welcome-title">WELCOME TO <span>LANTERNFIELD ADVISORY GROUP</span></h2>
  <p class="abs welcome-text" style="top:78px">Lorem ipsum dolor sit amet, consectetur adipisicing elit, sed do eiusmod tempor incididunt ut labore et dolore magna aliqua incididunt ut labore et dolore magna aliqua. Ut enim ad minimveniam, quis nostrud exercitation laboris.</p>
  <p class="abs welcome-text" style="top:144px">Ut enim ad minim veniam, quis nostrud exercitation ullamco laboris nisi ut aliquip ex ea commodo consequat.</p>
  <div class="abs read-more"><svg width="10" height="12" viewBox="0 0 10 12"><path d="M0 0l10 6-10 6z" fill="var(--green)"/></svg>READ MORE</div>
</section>

<section>
  <svg width="0" height="0" style="position:absolute">
    <defs>
      <symbol id="cal" viewBox="0 0 44 66">
        <rect x="2" y="6" width="40" height="36" fill="#fff" stroke="var(--lime)" stroke-width="3"/>
        <rect x="2" y="6" width="40" height="6" fill="var(--lime)"/>
        <rect x="10" y="1" width="4" height="9" fill="var(--lime)"/>
        <rect x="30" y="1" width="4" height="9" fill="var(--lime)"/>
      </symbol>
    </defs>
  </svg>

  <article class="abs post" style="left:154px;top:872px">
    <svg class="abs post-date" viewBox="0 0 44 66"><use href="#cal"/><text x="22" y="35" text-anchor="middle" font-family="Oswald,sans-serif" font-size="17" fill="var(--blue)">17</text></svg>
    <div class="abs post-month">MAR</div>
    <h3 class="abs post-title">Brand Equity &amp; Positioning</h3>
    <p class="abs post-body">Lorem ipsum dolor sit amet, consectetur adipisicing elit, sed do eiusmod tempor incididunt ut labore et dolore magna aliqua. Ut enim ad minim veniam, quis nostrud exercitation laboris.</p>
  </article>
  <article class="abs post" style="left:614px;top:872px">
    <svg class="abs post-date" viewBox="0 0 44 66"><use href="#cal"/><text x="22" y="35" text-anchor="middle" font-family="Oswald,sans-serif" font-size="17" fill="var(--blue)">28</text></svg>
    <div class="abs post-month">MAR</div>
    <h3 class="abs post-title">Millions could go off blood pressure meds</h3>
    <p class="abs post-body">Lorem ipsum dolor sit amet, consectetur adipisicing elit, sed do eiusmod tempor incididunt ut labore et dolore magna aliqua. Ut enim ad minim veniam, quis nostrud exercitation laboris.</p>
  </article>
  <article class="abs post" style="left:154px;top:1001px">
    <svg class="abs post-date" viewBox="0 0 44 66"><use href="#cal"/><text x="22" y="35" text-anchor="middle" font-family="Oswald,sans-serif" font-size="17" fill="var(--blue)">02</text></svg>
    <div class="abs post-month">FEB</div>
    <h3 class="abs post-title">Raising import duties on paper to hurt students most</h3>
    <p class="abs post-body">Lorem ipsum dolor sit amet, consectetur adipisicing elit, sed do eiusmod tempor incididunt ut labore et dolore magna aliqua. Ut enim ad minim veniam, quis nostrud exercitation laboris.</p>
  </article>
  <article class="abs post" style="left:614px;top:1001px">
    <svg class="abs post-date" viewBox="0 0 44 66"><use href="#cal"/><text x="22" y="35" text-anchor="middle" font-family="Oswald,sans-serif" font-size="17" fill="var(--blue)">23</text></svg>
    <div class="abs post-month">FEB</div>
    <h3 class="abs post-title">Photo blog inspires fashion journalist to an entrepreneur</h3>
    <p class="abs post-body">Lorem ipsum dolor sit amet, consectetur adipisicing elit, sed do eiusmod tempor incididunt ut labore et dolore magna aliqua. Ut enim ad minim veniam, quis nostrud exercitation laboris.</p>
  </article>
  <article class="abs post" style="left:154px;top:1132px">
    <svg class="abs post-date" viewBox="0 0 44 66"><use href="#cal"/><text x="22" y="35" text-anchor="middle" font-family="Oswald,sans-serif" font-size="17" fill="var(--blue)">25</text></svg>
    <div class="abs post-month">JAN</div>
    <h3 class="abs post-title">Raising import duties on paper to hurt students most</h3>
    <p class="abs post-body">Lorem ipsum dolor sit amet, consectetur adipisicing elit, sed do eiusmod tempor incididunt ut labore et dolore magna aliqua. Ut enim ad minim veniam, quis nostrud exercitation laboris.</p>
  </article>
  <article class="abs post" style="left:614px;top:1132px">
    <svg class="abs post-date" viewBox="0 0 44 66"><use href="#cal"/><text x="22" y="35" text-anchor="middle" font-family="Oswald,sans-serif" font-size="17" fill="var(--blue)">14</text></svg>
    <div class="abs post-month">DEC</div>
    <h3 class="abs post-title">Photo blog inspires fashion journalist to an entrepreneur</h3>
    <p class="abs post-body">Lorem ipsum dolor sit amet, consectetur adipisicing elit, sed do eiusmod tempor incididunt ut labore et dolore magna aliqua. Ut enim ad minim veniam, quis nostrud exercitation laboris.</p>
  </article>
</section>

<section class="abs testimonials" role="img" aria-label="Green-tinted photo of smiling office colleagues">
  <h2 class="abs section-title-light">OUR TESTIMONIALS</h2>
  <div class="abs avatar" style="left:218px;top:128px" role="img" aria-label="Portrait of a male client"></div>
  <div class="abs avatar" style="left:539px;top:128px" role="img" aria-label="Portrait of a male client"></div>
  <div class="abs avatar" style="left:873px;top:128px" role="img" aria-label="Portrait of a female client"></div>

  <blockquote class="abs quote" style="left:150px;top:240px">
    <div class="quote-mark">&ldquo;</div>
    <p class="quote-text">Vel illum dolore eu feugiat nulla facilisis at vero eros et accumsan et iusto dignissim qui blandit praesent lupt zril delenit augue duis dolore te feugait nulla facilisi.</p>
    <div class="quote-name">Marcus Delacroix</div>
    <div class="quote-role">Accounting Officer</div>
  </blockquote>
  <blockquote class="abs quote" style="left:469px;top:240px">
    <div class="quote-mark">&ldquo;</div>
    <p class="quote-text">Typi non habent claritatem insitam est us legentis in iis qui facit eorum claritatem. Investigationes demonstraverunt lectores legere me lius quod ii legunt saepius.</p>
    <div class="quote-name">Owen Halvorsen</div>
    <div class="quote-role">Accounting Officer</div>
  </blockquote>
  <blockquote class="abs quote" style="left:798px;top:240px">
    <div class="quote-mark">&ldquo;</div>
    <p class="quote-text">Claritas est etiam processus dynamicus sequitur mutationem consuetudium lectorum. Mirum est notare quam littera gothica, quam nunc pumus parum clam, anteposuerit litterarum formas.</p>
    <div class="quote-name">Celeste Varona</div>
    <div class="quote-role">President, CEO of Brightwave Systems</div>
  </blockquote>
</section>

<section>
  <h2 class="abs contact-title">CONTACT US</h2>
  <p class="abs contact-sub">Get ahead of the curve and contact us for more information.</p>
  <div class="abs field" style="left:159px;top:1882px;width:410px;height:54px">Name *</div>
  <div class="abs field" style="left:159px;top:1943px;width:410px;height:54px">Email *</div>
  <div class="abs field" style="left:159px;top:2005px;width:410px;height:54px">Company</div>
  <div class="abs field" style="left:591px;top:1882px;width:433px;height:115px;padding-top:14px">Your Message</div>
  <div class="abs send" style="left:591px;top:2005px;width:433px;height:54px">
    <svg width="30" height="20" viewBox="0 0 30 20"><rect x="1" y="1" width="28" height="18" fill="none" stroke="#fff" stroke-width="1.5"/><path d="M1 1l14 10 14-10M1 19l10-8M29 19l-10-8" fill="none" stroke="#fff" stroke-width="1.5"/></svg>
  </div>
</section>

<footer class="abs footer">
  <div class="abs foot-h" style="left:146px;top:30px"><b>Feel free</b> to contact us</div>
  <p class="abs foot-text" style="left:146px;top:55px;width:480px">At vero eos et accusamus et iusto odio dignissimos ducimus, qui blanditiis praesentium voluptatum deleniti atque corrupti, quos dolores et quas molestias excepturi sint."</p>
  <div class="abs sub-input" style="left:145px;top:94px;width:375px;height:31px"></div>
  <div class="abs sub-btn" style="left:532px;top:94px;width:112px;height:31px">Subscribe</div>

  <div class="abs foot-h" style="left:784px;top:34px"><b>Our</b> location</div>
  <p class="abs foot-text" style="left:784px;top:60px">14 Harbor Lane<br>Millbrook, NH 03099<br>info@lanternfieldadvisory.com</p>

  <nav class="abs foot-links" style="left:146px;top:190px"><span>Home</span><span>About Us</span><span>Terms</span><span>Privacy</span></nav>
  <div class="abs foot-text" style="left:786px;top:191px;font-size:11.5px;color:#fff">Lanternfield Advisory &copy; 2013. All Rights Reserved</div>
</footer>

</body>
</html>
```